Business Card Design for new consultancy company

Name of Company: Cobalt Wayline
Nature of Business: Digital Business Consultancy
Specialises in Digital Media Strategy, Digital Business Model Transformation, Over-The-Top (OTT) Development, Web Business Development, Digital Marketing, Web and App Product Development, Design and Innovation

Website: http://www.cobalt-wayline.example

Designs can be of any colour or any number of colours, objective is to give the impression we are a digital trend setter, creative and impactful.

Also please suggest a logo to complement the name and business card.

Target Market(s)

Media Companies, Telcos, Enterprises

Industry/Entity Type

Business

Contact Information for Business Card

Standard business card size. OK with to play with small variations like corners for impact/impression.

Font styles to use
Serif
Sans Serif

Requirements
Must have
• Clarity, Impact, Creativity
Nice to have
• Design should encapsulate professionalism, expertise, yet trend-setting and vibrant for digital consultancy
Should not have
• Messy layout, too gaudy colours or design

```html
<!DOCTYPE html>
<html lang="en">
<head>
<meta charset="utf-8">
<title>Cobalt Wayline — Business Card</title>
<link rel="stylesheet" href="https://fonts.googleapis.com/css2?family=Alegreya+Sans:wght@400;500;700&display=swap">
<style>
  :root {
    --page-bg: #e4e4e4;
    --cobalt-light: #3788a8;
    --cobalt-deep: #234f7d;
    --ink-white: #f2f5f8;
    --card-shadow: rgba(0, 0, 0, 0.18);
  }
  * { box-sizing: border-box; margin: 0; padding: 0; }
  html, body {
    width: 1200px;
    height: 1200px;
    overflow: hidden;
    background: var(--page-bg);
    font-family: "Alegreya Sans", sans-serif;
    color: var(--ink-white);
  }
  .sheet {
    width: 1200px;
    height: 1200px;
    display: flex;
    flex-direction: column;
    align-items: center;
    justify-content: center;
    gap: 56px;
  }
  .card {
    position: relative;
    width: 900px;
    height: 514px;
    overflow: hidden;
    background: var(--cobalt-light);
    box-shadow: 0 10px 28px var(--card-shadow);
    text-align: center;
  }
  .band {
    position: absolute;
    left: 0;
    width: 100%;
    background: var(--cobalt-deep);
  }
  .brand-mark {
    display: block;
    margin: 0 auto;
    border-radius: 50%;
    border: 6px solid var(--ink-white);
  }
  .brand-name {
    font-weight: 700;
    line-height: 1.05;
    letter-spacing: 0.5px;
  }
  .brand-tagline {
    font-weight: 400;
    line-height: 1.2;
  }
  .web-address {
    font-weight: 700;
    letter-spacing: 0.5px;
  }

  /* Front side */
  .card--front .identity {
    position: absolute;
    top: 66px;
    left: 0;
    width: 100%;
  }
  .card--front .brand-mark { width: 92px; height: 92px; margin-bottom: 22px; }
  .card--front .brand-name { font-size: 46px; }
  .card--front .brand-tagline { font-size: 27px; margin-top: 6px; }
  .card--front .band--footer { top: 372px; height: 142px; }
  .card--front .web-address {
    position: absolute;
    top: 372px;
    left: 0;
    width: 100%;
    line-height: 142px;
    font-size: 38px;
  }

  /* Back side */
  .card--back .band--top { top: 0; height: 40px; }
  .card--back .band--footer { top: 352px; height: 162px; }
  .card--back .rule--accent {
    position: absolute;
    left: 0;
    top: 440px;
    width: 100%;
    height: 8px;
    background: var(--cobalt-light);
  }
  .card--back .identity {
    position: absolute;
    top: 58px;
    left: 0;
    width: 100%;
  }
  .card--back .brand-mark { width: 66px; height: 66px; border-width: 5px; margin-bottom: 12px; }
  .card--back .brand-name { font-size: 36px; }
  .card--back .brand-tagline { font-size: 22px; margin-top: 4px; }
  .specialities {
    margin-top: 14px;
    font-size: 18px;
    font-weight: 500;
    line-height: 1.4;
    padding: 0 60px;
  }
  .card--back .web-address {
    position: absolute;
    top: 352px;
    left: 0;
    width: 100%;
    line-height: 88px;
    font-size: 34px;
  }
</style>
</head>
<body>
<main class="sheet">

  <section class="card card--front" aria-label="Business card front">
    <div class="identity">
      <span class="brand-mark" aria-hidden="true"></span>
      <p class="brand-name">Cobalt Wayline</p>
      <p class="brand-tagline">(Digital Business Consultancy)</p>
    </div>
    <div class="band band--footer"></div>
    <p class="web-address">www.cobalt-wayline.example</p>
  </section>

  <section class="card card--back" aria-label="Business card back">
    <div class="band band--top"></div>
    <div class="identity">
      <span class="brand-mark" aria-hidden="true"></span>
      <p class="brand-name">Cobalt Wayline</p>
      <p class="brand-tagline">(Digital Business Consultancy)</p>
      <p class="specialities">
        Specialises in Digital Media Strategy, Digital Business Model Transformation,<br>
        Over-The-Top (OTT) Development, Web Business Development,<br>
        Digital Marketing, Web and App Product Development, Design and Innovation
      </p>
    </div>
    <div class="band band--footer"></div>
    <p class="web-address">www.cobalt-wayline.example</p>
    <div class="rule--accent"></div>
  </section>

</main>
</body>
</html>
```